Spa Business Card Design Project

Hello! We are a boutique spa for men and women that is rebranding. I would like a memorable new business card that showcases our beautiful new logo and our unique business. I would like it to be classic/timeless and eclectic/artistic at the  same time.
I am a fan of negative space as you can tell from the logo. I am also open to any creative ideas.
Multi sided design. Two sided design is acceptable as an option, too. "Flaps/folds/whatever the design term is" are optional- whether full vertical or horizontal, half flap, full flap etc
On either side next to the golden snail I would potentially like to see "slow down. Enjoy Life."  Possibly on one statment on top of each other, crowned with the snail. Or the statment following the snail on one line... I am open for a creative suprise, too.
The back I would like room for the standard Information
"3817 Birch Lane
Ashgrove, Vermont 05043
(518) 462 3085
info@thecorvella spa.com
The snail is to be done in gold ink.
Can I also Have an option for cards that are individualized for staff members, too?

Updates
Project Deadline Extended
Reason: I apologize for the deadline extension. My day was more involved than anticipated in other matters. Hope to have this closed by next Tuesday.
Thank you

Target Market(s)
Men and women with expendable income between the ages of 30-55
Industry/Entity Type
Boutique
Requirements
Must have
- only black and gold ink.

Nice to have
- One of a kind.
Showcase the snail :-)
make you smile :-)
Fun, but professional.
Should not have
- Lots of color.
Too feminine.
Too busy.

```html
<!DOCTYPE html>
<html lang="en">
<head>
<meta charset="utf-8">
<title>The Corvella Spa — Business Card</title>
<link rel="stylesheet" href="https://fonts.googleapis.com/css2?family=Cinzel:wght@400&family=Libre+Baskerville:wght@400&family=Mulish:wght@400&display=swap">
<style>
  :root {
    --backdrop: #cdd6d6;
    --card: #fde28e;
    --ink: #141414;
    --bar-black: #111111;
    --bar-olive: #7b7150;
    --pattern: #e6c878;
    --pattern-deep: #d9bb6e;
    --label: #9a5420;
    --faint: #e9cd84;
    --shadow: rgba(0, 0, 0, 0.55);
  }
  * { box-sizing: border-box; margin: 0; padding: 0; }
  html, body { width: 1200px; height: 846px; overflow: hidden; }
  body { background: var(--backdrop); position: relative; font-family: "Libre Baskerville", serif; color: var(--ink); }

  .card { position: absolute; background: var(--card); box-shadow: 2px 3px 0 var(--shadow); overflow: hidden; }
  .card--front { left: 20px; top: 35px; width: 735px; height: 422px; }
  .card--back { left: 768px; top: 35px; width: 420px; height: 736px; }

  .pattern { position: absolute; }
  .front-paisley { left: 0; top: 60px; width: 200px; height: 362px;
    background: radial-gradient(ellipse at 30% 60%, var(--pattern-deep), var(--pattern) 70%, transparent 72%); }
  .front-corner { right: 0; top: 0; width: 90px; height: 110px;
    background: radial-gradient(ellipse at 60% 50%, var(--pattern-deep), transparent 70%); }
  .back-corner { left: 0; top: 0; width: 110px; height: 90px;
    background: radial-gradient(ellipse at 40% 40%, var(--pattern-deep), transparent 70%); }

  .bar { position: absolute; }
  .bar--front-top { left: 0; top: 13px; width: 618px; height: 9px; background: var(--bar-black); }
  .bar--front-bottom { left: 191px; top: 396px; width: 544px; height: 9px; background: var(--bar-black); }
  .bar--back-left { left: 14px; top: 115px; width: 9px; height: 621px; background: var(--bar-olive); }
  .bar--back-right { left: 395px; top: 0; width: 9px; height: 543px; background: var(--bar-olive); }

  .brand { position: absolute; text-align: center; font-family: "Libre Baskerville", serif; color: var(--ink); line-height: 1.05; }
  .brand__mark { display: inline-block; width: 9px; height: 9px; border-radius: 50%; background: var(--ink); vertical-align: middle; margin-right: 8px; }
  .brand--front { left: 180px; top: 118px; width: 440px; font-size: 50px; }
  .brand--back-top { left: 60px; top: 40px; width: 300px; font-size: 32px; }
  .brand--back-small { left: 110px; top: 236px; width: 200px; font-size: 19px; line-height: 1.2; }
  .brand--watermark { left: 20px; top: 572px; width: 390px; font-size: 46px; color: var(--faint); }

  .tagline { position: absolute; font-family: "Mulish", sans-serif; color: var(--ink); text-align: center; }
  .tagline--front { left: 180px; top: 283px; width: 440px; font-size: 18px; }
  .tagline--back { left: 60px; top: 139px; width: 300px; font-size: 12px; }

  .contact { position: absolute; left: 40px; top: 310px; width: 305px; text-align: center; font-size: 17px; line-height: 21px; }
  .contact__label { color: var(--label); font-size: 16px; margin-bottom: 4px; }
  .contact__group { margin-bottom: 15px; }

  .side-label { position: absolute; font-family: "Cinzel", serif; font-size: 33px; letter-spacing: 2px; color: var(--ink); }
  .side-label--front { left: 314px; top: 466px; }
  .side-label--back { left: 936px; top: 779px; }
</style>
</head>
<body>

<section class="card card--front" aria-label="Card front">
  <div class="pattern front-paisley" role="img" aria-label="Large golden paisley and concentric circle pattern"></div>
  <div class="pattern front-corner" role="img" aria-label="Small paisley ornament"></div>
  <div class="bar bar--front-top"></div>
  <div class="bar bar--front-bottom"></div>
  <div class="brand brand--front"><span class="brand__mark"></span>THE<br>CORVELLA<br>SPA</div>
  <p class="tagline tagline--front">a boutique spa for Men &amp; Women</p>
</section>
<p class="side-label side-label--front">FRONT</p>

<section class="card card--back" aria-label="Card back">
  <div class="pattern back-corner" role="img" aria-label="Small paisley ornament"></div>
  <div class="bar bar--back-left"></div>
  <div class="bar bar--back-right"></div>
  <div class="brand brand--back-top">THE<br>CORVELLA SPA</div>
  <p class="tagline tagline--back">a boutique spa for Men &amp; Women</p>
  <div class="brand brand--back-small">THE<br>CORVELLA SPA</div>
  <div class="contact">
    <div class="contact__group">
      <p class="contact__label">Address...</p>
      <p>NO:-3817 Birch Lane</p>
      <p>Ashgrove,</p>
      <p>Vermont 05043</p>
    </div>
    <div class="contact__group">
      <p class="contact__label">Contact...</p>
      <p>(518) 462 3085</p>
    </div>
    <div class="contact__group">
      <p class="contact__label">Email...</p>
      <p>info@thecorvella spa.com</p>
    </div>
  </div>
  <div class="brand brand--watermark" aria-hidden="true">THE<br>CORVELLA<br>SPA</div>
</section>
<p class="side-label side-label--back">BACK</p>

</body>
</html>
```